依頼詳細
表面はカラー、裏面は白黒で申し込み用紙にしようと考えています。
魅力のあるツアーだと思いますので、読み手に伝わるよう作成をお願いします。
〈ツアーのポイント〉
・透き通った青い海、緑の山々、満天の星空など、大自然に囲まれたダイナミックな眺望
・貸切バスで観光スポットをご案内
・地元の食材にこだわった料理を堪能
・島人との交流
・自然の中でBBQ、キャンプファイヤー
・宿泊は神津島唯一の温泉宿
・カップル成立で特典付き
・格安
など
多少変更が出るかもしれませんので、こちらでも編集できる形式で納品をお願いします。
ご不明点などありましたらご連絡ください。
よろしくお願いいたします。
記載項目
表現など変更して頂いて結構です。

【表面】
独身女性参加者募集
〈イベント名称〉渚トーク星結び
〈日時〉2015年7月3日(金)~2015年7月5日(日)
〈会場〉神津島
〈ツアースケジュール〉
1日目 20:00 東京 灯波客船ターミナル集合(女性のみ)・女子会
23:00 出航(大型客船)
2日目 9:00 神津島着・チェックイン
朝 男性合流・アイスブレイク
昼 昼食・島内観光
夜 BBQ・キャンプファイヤー・温泉旅館宿泊
3日目 朝 自由時間
13:35 神津島発
17:30 東京 灯波客船ターミナル着・解散
〈ツアーのポイント〉依頼詳細参考
〈集合場所〉白浪航路灯波港 1階ロビー ※若葉環状線蓮見坂駅から徒歩8分
〈集合時間〉2015年7月3日(金)20:00
〈参加対象〉20歳~35歳の島外在住独身女性
〈募集人数〉15名(先着順)
〈参加料金〉15,000円/1人(交通費・宿泊費・食費込み)
〈申込方法〉裏面の申込書にご記入の上、メール・FAX・郵送にてお申込みください。
〈申込締切〉2015年6月7日(日)
〈ホームページ〉
※ホームページのURLを載せたいのですが、まだ出来上がっていないので後ほどURLを追加できるようにしていただきたいです。

裏面は補足情報に記載します。
サイズ
A4
ページ数
両面
希望イメージ
• +5 0 +5
• シンプル
複雑
• 単色
カラフル
• 暗い
明るい
• 日常
高級
• 遊び心
厳粛
• 未来的
伝統的
• 女性的
男性的
希望する色
赤系、水色系、緑系、黄・オレンジ系
納品ファイル
補足説明
【裏面】申込用紙
〈イベント名称〉
〈日時〉
〈会場〉
〈募集人数〉15名(先着順)
〈参加資格〉20歳から35歳までの神津島外在住の独身女性
お一人様参加・シングルマザー・結婚歴あり歓迎
〈参加料金〉
MAIL  shiomi@hx.nagisanet-example.jp
メールでのお申し込みは①氏名②生年月日③住所④電話番号⑤メールアドレスを添えて上記のアドレスまでご送信ください。
FAX 04992-7-5530
〈申し込みフォーム〉
・氏名(ふりがな)
・氏名
・生年月日
・電話番号
・メールアドレス
・自己PR
〈注意事項〉
1 申し込み・キャンセルは6月7日(日)までにお願いします。
2 男女比は出来る限り調整しますが同数にならないこともありますのでご了承願います。
3 個人情報は厳重に管理し、本事業のみの使用とさせていただきます。
4 悪天候時はプログラム内容を変更または中止する場合があります。

申し込み受付後、事務局より順次詳細をお送りいたします。

問い合わせ・お申込み 汐見村商工会青年部事務局
〒100-0999 東京都汐見村汐見村2483番地
TEL  04992-7-4418
FAX  04992-7-5530

依頼公開後の追記内容
写真を添付します。

ターゲット層を対象にアンケート調査を実施した結果、最も多く票が集まったため。

この度は私どもの為に、多数ご提案をご用意していただき、誠にありがとうございます。どの提案も魅力を感じていましたが、上記の理由から一社選ばせていただきました。
折角親身にお世話をしていただいたところ、心苦しい限りですが、ご理解いただければ幸いです。
また、同様の機会があればよろしくお願いいたします。

```html
<!DOCTYPE html>
<html lang="ja">
<head>
<meta charset="utf-8">
<title>渚トーク星結び 独身女性参加者募集</title>
<link rel="stylesheet" href="https://fonts.googleapis.com/css2?family=Mochiy+Pop+One&family=M+PLUS+Rounded+1c:wght@500;700;800&family=Zen+Maru+Gothic:wght@700;900&display=swap">
<style>
:root{
  --red:#e4322b;
  --red-soft:#f7c9c6;
  --pink:#fdeeed;
  --blue:#1c6fb8;
  --navy:#1d3f7a;
  --ink:#333;
  --sea-a:#2f9fd0;
  --sea-b:#7fd2e6;
  --green:#5f9d4b;
  --white:#fff;
}
*{margin:0;padding:0;box-sizing:border-box}
html,body{width:851px;height:1200px;overflow:hidden;background:var(--white)}
body{font-family:"M PLUS Rounded 1c",sans-serif;color:var(--ink)}
.flyer{position:relative;width:851px;height:1200px;border:12px solid var(--red-soft);background:var(--white)}
.title-block{position:absolute;left:0;right:0;top:18px;text-align:center}
.title-kana{font-family:"M PLUS Rounded 1c",sans-serif;font-weight:800;color:var(--red);font-size:20px;letter-spacing:4px}
.title{font-family:"Mochiy Pop One",sans-serif;color:var(--red);font-size:96px;line-height:1.1;letter-spacing:2px}
.title small{font-size:52px;color:var(--red)}
.date{font-family:"Zen Maru Gothic",sans-serif;font-weight:900;color:var(--blue);font-size:36px;margin-top:6px}
.date .arrow{font-size:26px;vertical-align:3px;margin:0 4px}
.photo-main{position:absolute;left:28px;top:290px;width:771px;height:300px;border-radius:12px;
  background:linear-gradient(180deg,#bfe3f4 0%,var(--sea-b) 35%,var(--sea-a) 60%,var(--green) 100%)}
.photo-inset{position:absolute;right:40px;top:420px;width:230px;height:150px;border:4px solid var(--white);border-radius:6px;
  background:linear-gradient(160deg,#1a5ea8,#3fa6d8)}
.headline{position:absolute;left:0;right:0;top:608px;text-align:center;font-family:"Zen Maru Gothic",sans-serif;font-weight:900;
  color:var(--red);font-size:62px;letter-spacing:2px}
.lead{position:absolute;left:0;right:0;top:698px;text-align:center;font-weight:800;color:var(--navy);font-size:25px;line-height:1.55}
.info{position:absolute;left:38px;top:800px;width:410px;font-size:17px;line-height:1.45}
.info-row{display:flex;gap:10px;margin-bottom:9px}
.info-label{flex:0 0 96px;background:var(--red);color:var(--white);font-weight:700;font-size:15px;text-align:center;border-radius:3px;height:24px;line-height:24px}
.info-text{font-weight:700;color:var(--ink)}
.info-text small{font-size:14px;font-weight:500}
.schedule{position:absolute;left:470px;top:790px;width:340px;height:330px;border:3px solid var(--red);border-radius:14px;background:var(--pink);padding:16px 16px}
.schedule-title{display:flex;align-items:center;justify-content:center;gap:8px;font-weight:800;color:var(--red);font-size:22px;margin-bottom:10px}
.day{display:flex;gap:6px;font-size:14px;line-height:1.5;margin-bottom:6px}
.day-num{flex:0 0 28px;height:28px;border-radius:50%;background:var(--red);color:var(--white);font-weight:800;text-align:center;line-height:28px;font-size:14px}
.day ul{list-style:none}
.day li{display:flex;gap:6px}
.day li b{flex:0 0 42px;color:var(--red)}
.url-bar{position:absolute;left:28px;right:28px;bottom:26px;height:40px;background:var(--red);color:var(--white);border-radius:20px;
  text-align:center;line-height:40px;font-weight:700;font-size:18px;letter-spacing:1px}
</style>
</head>
<body>
<main class="flyer">
  <header class="title-block">
    <p class="title-kana">nagisa-talk ♥</p>
    <h1 class="title">渚トーク<small>星結び</small></h1>
    <p class="date">2015年7月3日(金)<span class="arrow">▶</span>7月5日(日)</p>
  </header>

  <div class="photo-main" role="img" aria-label="透き通った青い海と緑の山、白い浜辺の島の海岸風景写真"></div>
  <div class="photo-inset" role="img" aria-label="青い海の中を泳ぐ魚の写真"></div>

  <h2 class="headline">独身女性参加者募集！</h2>
  <p class="lead">透き通った青い海、緑の山々、満天の星空……<br>大自然に囲まれたロマンチックな島で、恋をしませんか？</p>

  <section class="info">
    <div class="info-row"><span class="info-label">【参加対象】</span><span class="info-text">20歳～35歳の島外在住独身女性</span></div>
    <div class="info-row"><span class="info-label">【募集人数】</span><span class="info-text">15名(先着順)</span></div>
    <div class="info-row"><span class="info-label">【参加料金】</span><span class="info-text">15,000円／1人<br><small>(交通費・宿泊費・食費込み)</small></span></div>
    <div class="info-row"><span class="info-label">【集合場所】</span><span class="info-text">白浪航路灯波港 1階ロビー<br><small>※若葉環状線蓮見坂駅から徒歩8分</small></span></div>
    <div class="info-row"><span class="info-label">【集合時間】</span><span class="info-text">2015年7月3日(金) 20時00分</span></div>
    <div class="info-row"><span class="info-label">【申込方法】</span><span class="info-text"><small>裏面の申込書にご記入の上、Eメール・FAX・郵送にてお申込みください。</small></span></div>
    <div class="info-row"><span class="info-label">【申込締切】</span><span class="info-text">2015年6月7日(日)</span></div>
  </section>

  <section class="schedule">
    <h3 class="schedule-title">
      <svg width="22" height="20" viewBox="0 0 22 20" aria-hidden="true"><path d="M11 19 L2 9 A5 5 0 0 1 11 3 A5 5 0 0 1 20 9 Z" fill="#e4322b"/></svg>
      ツアースケジュール
    </h3>
    <div class="day"><span class="day-num">1日</span><ul>
      <li><b>20:00</b><span>東京 灯波客船ターミナル集合<br>(女性のみ)・女子会</span></li>
      <li><b>23:00</b><span>出航(大型客船)</span></li></ul></div>
    <div class="day"><span class="day-num">2日</span><ul>
      <li><b>9:00</b><span>神津島着・チェックイン</span></li>
      <li><b>朝</b><span>男性合流・アイスブレイク</span></li>
      <li><b>昼</b><span>昼食・島内観光</span></li>
      <li><b>夜</b><span>BBQ・キャンプファイヤー・<br>温泉旅館宿泊</span></li></ul></div>
    <div class="day"><span class="day-num">3日</span><ul>
      <li><b>朝</b><span>自由時間</span></li>
      <li><b>13:35</b><span>神津島発</span></li>
      <li><b>17:30</b><span>東京 灯波客船ターミナル着・解散</span></li></ul></div>
  </section>

  <footer class="url-bar">http://○○○○○○○○○○○○○○○○○○○○○○○○○○○</footer>
</main>
</body>
</html>
```